Discreet simple classy for adult entertainment

I would like a matte black business card with gold writing for my business. Keeping it simple. Having my following:

Lana frost
Events. Entertainment. Promotions
0491726580

or alternatively could have what i had on my previous card below but i think i prefer the above as again - discretion.

Maybe a nice gold line thru the card or some other very simple design . Or not open to ideas/ can be doublesided if any good ideas with that.

included pics of my old bus card. not sure weather i want a photo on it or not. if i do it wont be the same pic. i kinda wanted a card that was discreet so if it was in someones wallet they wouldn't neccessarily realise it was from a stripper.

Target Market(s)

men

Industry/Entity Type

Business

Contact Information for Business Card

Lana frost
0491726580

Requirements
Nice to have
• i don't know i am really open to anything. im giving my cards to guys so something they can have in their wallet that is discreet preferably.

```html
<!DOCTYPE html>
<html lang="en">
<head>
<meta charset="utf-8">
<title>Lana frost — Business Card</title>
<link rel="stylesheet" href="https://fonts.googleapis.com/css2?family=Great+Vibes&family=Cabin:wght@400&display=swap">
<style>
  :root {
    --page: #ffffff;
    --card: #231f20;
    --gold: #c9a063;
    --gold-soft: #b98f55;
  }
  html, body {
    margin: 0;
    padding: 0;
    width: 1200px;
    height: 960px;
    overflow: hidden;
    background: var(--page);
  }
  .canvas {
    position: relative;
    width: 1200px;
    height: 960px;
  }
  .card {
    position: absolute;
    left: 70px;
    top: 176px;
    width: 1060px;
    height: 604px;
    background: var(--card);
    overflow: hidden;
  }
  .name {
    position: absolute;
    margin: 0;
    font-family: "Great Vibes", cursive;
    font-weight: 400;
    color: var(--gold);
    line-height: 1;
    white-space: nowrap;
  }
  .name__first {
    left: 100px;
    top: 95px;
    font-size: 235px;
  }
  .name__last {
    left: 425px;
    top: 258px;
    font-size: 240px;
  }
  .services {
    position: absolute;
    left: 44px;
    top: 404px;
    width: 360px;
    margin: 0;
    padding: 0;
    list-style: none;
    text-align: center;
    font-family: "Cabin", sans-serif;
    font-size: 37px;
    line-height: 50px;
    color: var(--gold-soft);
  }
  .phone {
    position: absolute;
    left: 670px;
    top: 490px;
    margin: 0;
    font-family: "Cabin", sans-serif;
    font-size: 44px;
    letter-spacing: 1px;
    color: var(--gold-soft);
  }
</style>
</head>
<body>
  <main class="canvas">
    <section class="card" aria-label="Business card">
      <h1 class="name name__first">Lana</h1>
      <p class="name name__last">frost</p>
      <ul class="services">
        <li>Events</li>
        <li>Entertainment</li>
        <li>Promotions</li>
      </ul>
      <p class="phone">0491726580</p>
    </section>
  </main>
</body>
</html>
```